Geschäftspapiere für Gärtnerei
Zielgruppe
Wir sind eine insektenfreundliche Gärtnerei und produzieren und handeln Stauden, Kräuter, Wildobst, Vogelschutzhecken, Vogelnährgehölze. Wir planen instektenfreundliche Gärten und Neuanlagen und beraten zu den Themen Naturgarten, antiautoritärer Garten, New German Style und Blackboxgardening.
Außerdem wachsen bei uns pestizidfreie Schnittblumen (Slowflowers).
Zielgruppe ist überwiegend aber nicht ausschließlich weiblich (zwischen ca. 24 - 50 Jahre Hauptzielgruppe), Balkonbesitzer*innen, neue Eigenheimbestitzer*innen, Brautpaare, Schrebergärtner*innen
Aufgabenstellung
Schaut euch gern ab Sonntag Abend auch die Internetseite an.
Richtig cool fände ich es wenn in irgendeiner Ecke des Briefpapiers ein Insekt auftaucht. Dabei ist es mit egal ob Raupe, Hummel, Schmetterling oder Wurm.
Viel Spaß, ich freue mich auf eure Entwürfe.

```html
<!DOCTYPE html>
<html lang="de">
<head>
<meta charset="utf-8">
<title>Hof Malvina – Briefpapier</title>
<link href="https://fonts.googleapis.com/css2?family=Arimo:wght@400&family=Open+Sans:wght@400;600&display=swap" rel="stylesheet">
<style>
  :root{
    --backdrop:#e4e5e6;
    --paper:#ffffff;
    --maroon:#773d58;
    --ink:#4d4140;
    --body:#3a3a3a;
    --rule:#9a9a9a;
    --watermark:#ececec;
  }
  *{margin:0;padding:0;box-sizing:border-box}
  html,body{width:1200px;height:945px;overflow:hidden;background:var(--backdrop)}
  .letterhead{
    position:absolute;left:282px;top:20px;width:636px;height:905px;
    background:var(--paper);box-shadow:0 4px 14px rgba(0,0,0,.18);
    font-family:"Open Sans",sans-serif;color:var(--ink);
  }
  .top-band{position:absolute;left:0;top:0;width:100%;height:7px;background:var(--maroon)}
  .brand{position:absolute;right:36px;top:34px;width:170px;text-align:center}
  .brand-mark{display:block;width:14px;height:14px;margin:0 auto 10px;background:var(--maroon)}
  .brand-name{font-size:17px;letter-spacing:4px;font-weight:400;color:var(--ink)}
  .contact{
    position:absolute;left:430px;top:128px;padding-left:14px;
    border-left:1px solid var(--ink);font-size:8px;line-height:12px;
  }
  .contact .row{display:flex;align-items:center;gap:5px}
  .contact svg{width:8px;height:8px;fill:var(--maroon)}
  .sender-line{
    position:absolute;left:60px;top:214px;font-size:6.5px;
    border-bottom:.6px solid var(--ink);padding-bottom:1px;
  }
  .fold-mark{position:absolute;left:0;width:16px;height:1px;background:var(--rule)}
  .letter-body{
    position:absolute;left:92px;top:330px;width:465px;
    font-family:"Arimo",sans-serif;font-size:10.5px;line-height:13px;color:var(--body);
    text-align:justify;
  }
  .letter-body p{margin-bottom:13px}
  .signature{
    position:absolute;left:100px;top:575px;width:170px;height:42px;
    background:linear-gradient(90deg,#e8e8e8,#f4f4f4);border-radius:4px;
  }
  .butterfly-decor{
    position:absolute;left:120px;top:650px;width:270px;height:220px;
    background:radial-gradient(ellipse at center,var(--watermark) 0%,#f6f6f6 60%,rgba(255,255,255,0) 72%);
  }
  .footer{position:absolute;left:150px;right:30px;top:800px;display:flex;font-size:9px;line-height:12px}
  .footer-col{padding:0 18px;border-left:1px solid var(--ink)}
  .footer-col:first-child{border-left:none;padding-left:0}
  .bottom-band{
    position:absolute;left:0;bottom:0;width:100%;height:28px;background:var(--maroon);
    color:#fff;font-size:10px;text-align:center;line-height:28px;letter-spacing:.5px;
  }
</style>
</head>
<body>
<main class="letterhead">
  <div class="top-band"></div>

  <header class="brand">
    <span class="brand-mark"></span>
    <div class="brand-name">HOF MALVINA</div>
  </header>

  <address class="contact" style="font-style:normal">
    <div>Hof Malvina</div>
    <div>Lene Hartwig</div>
    <div>Lindenweg 42</div>
    <div>21390 Wiesenau in der Heide</div>
    <div class="row"><svg viewBox="0 0 10 10"><path d="M2 1l2 0 1 2-1 1c.6 1.2 1.4 2 2.6 2.6l1-1 2 1v2c0 .5-.5 1-1 1C4 9.6.4 6 0 2c0-.5.5-1 1-1z"/></svg>0170-555 21 904</div>
    <div class="row"><svg viewBox="0 0 10 10"><rect x="1" y="3" width="8" height="6" rx="1"/><rect x="2" y="1" width="6" height="2" rx="1"/></svg>04100-558811</div>
    <div class="row"><svg viewBox="0 0 10 10"><path d="M0 2h10v6H0z"/><path d="M0 2l5 3.5L10 2" stroke="#fff" stroke-width=".8" fill="none"/></svg>lene@hof-malvina.de</div>
  </address>

  <div class="sender-line">Hof Malvina | Lindenweg 42 | 21390 Wiesenau</div>

  <span class="fold-mark" style="top:318px"></span>
  <span class="fold-mark" style="top:452px"></span>
  <span class="fold-mark" style="top:618px"></span>

  <section class="letter-body">
    <p>Lorem ipsum dolor sit amet, consectetur adipiscing elit. Proin tincidunt, lectus id malesuada cursus, lorem augue egestas magna, ut mattis orci ante ut arcu. Sed mauris tellus, fermentum quis ligula nec, posuere pulvinar eros. Nam at mi quis velit pellentesque finibus. Donec lacus velit, faucibus mollis dolor nec, finibus pellentesque orci. Duis sed dictum elit, ut posuere arcu. Phasellus ac dolor et ante consequat rutrum nec nec tortor. Donec consequat, nibh sit amet pulvinar faucibus, turpis magna venenatis diam, vel pretium eros erat vestibulum nulla.</p>
    <p>Sed pretium ac enim eu viverra. Aliquam ac est eget magna convallis convallis. Aenean augue purus, finibus eget turpis quis, finibus dignissim nibh. Phasellus viverra lobortis dignissim. Duis varius turpis in sapien accumsan facilisis. Sed vehicula gravida diam a interdum. Nullam convallis ligula id erat egestas consequat. Integer consectetur ex vel aliquet iaculis. Vestibulum molestie sodales mauris, at tincidunt risus pellentesqu.</p>
    <p>Mauris facilisis, lectus at accumsan tincidunt, dui magna imperdiet sem, quis tempor est lectus eu ipsum. Praesent in fermentum nisl. Maecenas at lorem at odio interdum iaculis. Pellentesque cursus nulla nunc, ut suscipit nulla maximus et. Donec maximus rhoncus metus, vel laoreet nisi pretium sit amet. Donec posuere enim lectus, vitae aliquam augue tincidunt dignissim. Morbi vitae congue velit, quis elementum.</p>
  </section>

  <div class="signature" role="img" aria-label="Handschriftliche Unterschrift von Lene Hartwig"></div>

  <div class="butterfly-decor" role="img" aria-label="Zart graue Schmetterlings-Illustration als Hintergrundmotiv"></div>

  <footer class="footer">
    <div class="footer-col">Konten:<br>Grünfeld Bank<br>IBAN: DE00 1234 5678 9012 3456 00</div>
    <div class="footer-col">Heidebank Wiesenland eG<br>IBAN: DE00 9876 5432 1098 7654 00</div>
    <div class="footer-col">Steuernummer: 00/123/45678</div>
  </footer>

  <div class="bottom-band">www.hof-malvina.de</div>
</main>
</body>
</html>
```